Website Design In PSD for Travel Company

We are looking for a web designer to create a PSD of a TOURS AND TRAVEL COMPANY website.
You should design the following pages. But if you can find an innovative way of combining them we are here for it.
HOME
TOURS
CAR RENTAL
PACKAGES
CONTACT US/ABOUT US
BLOG

We are looking for a creative design and something different.

Incase you need more information as you design pls msg us

Here is an idea of something we want but make it better. https://brindlewaytoursgroup.example/

```html
<!DOCTYPE html>
<html lang="en">
<head>
<meta charset="utf-8">
<title>Tours &amp; Travel — Home</title>
<link href="https://fonts.googleapis.com/css2?family=Poppins:wght@400;500;600;700&display=swap" rel="stylesheet">
<style>
  :root {
    --page-bg: #e4eeeb;
    --deep-sea: #0b2420;
    --mid-sea: #174f45;
    --shallow-sea: #2f8a72;
    --white: #ffffff;
    --ink: #1d2523;
    --muted: #5d6664;
    --accent: #18a184;
    --nav-band: rgba(255, 255, 255, 0.08);
  }
  * { box-sizing: border-box; margin: 0; padding: 0; }
  html, body { width: 1200px; height: 904px; overflow: hidden; }
  body {
    background: var(--page-bg);
    font-family: "Poppins", sans-serif;
    color: var(--white);
    position: relative;
  }
  .hero {
    position: absolute;
    left: 0; top: 115px;
    width: 1200px; height: 673px;
    border-radius: 22px 22px 0 0;
    overflow: hidden;
  }
  .hero-photo {
    position: absolute; inset: 0;
    background:
      radial-gradient(ellipse 200px 300px at 800px 400px, rgba(205, 185, 170, 0.55), transparent 70%),
      radial-gradient(ellipse 380px 320px at 1120px 480px, rgba(70, 150, 110, 0.6), transparent 70%),
      radial-gradient(ellipse 300px 200px at 1100px 120px, rgba(60, 170, 150, 0.5), transparent 70%),
      linear-gradient(100deg, var(--deep-sea) 0%, #0f332d 35%, var(--mid-sea) 65%, var(--shallow-sea) 100%);
  }
  .brand {
    position: absolute; left: 93px; top: 46px;
    font-size: 14.5px; font-weight: 700; letter-spacing: 0.5px; line-height: 20px;
  }
  .main-nav {
    position: absolute; left: 481px; right: 0; top: 38px;
    height: 36px;
    background: var(--nav-band);
  }
  .main-nav a {
    position: absolute; top: 0; line-height: 36px;
    color: var(--white); text-decoration: none;
    font-size: 13px; font-weight: 500; letter-spacing: 0.4px;
    white-space: nowrap;
  }
  .headline-lead {
    position: absolute; left: 93px; top: 196px;
    font-size: 30px; font-weight: 500; line-height: 40px;
  }
  .headline {
    position: absolute; left: 91px; top: 222px;
    font-size: 64px; font-weight: 700; line-height: 86px;
  }
  .intro {
    position: absolute; left: 93px; top: 313px;
    width: 566px;
    border-left: 2px solid var(--white);
    padding-left: 16px;
    font-size: 12.5px; line-height: 20px; font-weight: 400;
  }
  .btn {
    position: absolute; top: 402px; height: 31px; width: 139px;
    display: flex; align-items: center; justify-content: center;
    font-size: 12px; border-radius: 2px; white-space: nowrap;
  }
  .btn-solid { left: 93px; background: var(--white); color: var(--ink); }
  .btn-outline { left: 252px; border: 1px solid var(--white); color: var(--white); }
  .slider-progress { position: absolute; left: 93px; top: 469px; }
  .social {
    position: absolute; left: 41px; top: 550px;
    display: flex; flex-direction: column; gap: 15px;
  }
  .social span {
    width: 13px; height: 13px; border-radius: 50%; background: var(--white);
  }
  .trip-search {
    position: absolute; left: 93px; top: 543px;
    width: 1013px; height: 84px;
    background: var(--white); border-radius: 7px;
    color: var(--ink);
  }
  .field { position: absolute; top: 20px; white-space: nowrap; }
  .field-label { font-size: 12px; line-height: 18px; color: var(--muted); }
  .field-value {
    margin-top: 5px; display: flex; align-items: center; gap: 12px;
    font-size: 12px; line-height: 18px; font-weight: 600;
  }
  .field-value svg { width: 13px; height: 13px; fill: var(--accent); margin-left: 4px; }
  .search-btn {
    position: absolute; left: 798px; top: 23px;
    width: 140px; height: 37px;
    background: var(--accent); color: var(--white);
    border-radius: 6px;
    display: flex; align-items: center; justify-content: center;
    font-size: 12px; white-space: nowrap;
  }
</style>
</head>
<body>
  <section class="hero">
    <div class="hero-photo" role="img" aria-label="Aerial photo of a rocky islet in clear turquoise sea"></div>

    <div class="brand">TOURS &amp; TRAVEL</div>
    <nav class="main-nav">
      <a href="#" style="left:31px">HOME</a>
      <a href="#" style="left:118px">TOURS</a>
      <a href="#" style="left:208px">CAR RENTAL</a>
      <a href="#" style="left:336px">PACKAGES</a>
      <a href="#" style="left:455px">CONTACT US</a>
      <a href="#" style="left:589px">BLOG</a>
    </nav>

    <p class="headline-lead">We have the best</p>
    <h1 class="headline">Destination</h1>
    <p class="intro">Lorem ipsum dolor sit amet, consectetur adipiscing elit. Ut nec tempus diam. Pellentesque eget varius elit. In vulputate velit tellus, eu rutrum lorem maximus et. Ut semper nunc at quam fringilla, ut facilisis augue sollicitudin.</p>

    <a class="btn btn-solid">Explore all trips</a>
    <a class="btn btn-outline">Explore packages</a>

    <svg class="slider-progress" width="250" height="12" viewBox="0 0 250 12">
      <circle cx="4" cy="6" r="4" fill="#fff"/>
      <line x1="28" y1="6" x2="245" y2="6" stroke="rgba(255,255,255,0.5)" stroke-width="1"/>
      <line x1="28" y1="6" x2="57" y2="6" stroke="#fff" stroke-width="2.5"/>
    </svg>

    <div class="social" aria-label="Social links">
      <span></span><span></span><span></span>
    </div>

    <form class="trip-search">
      <div class="field" style="left:75px">
        <div class="field-label">Destination</div>
        <div class="field-value">
          <svg viewBox="0 0 16 16"><path d="M15 1 1 7l6 2 2 6z"/></svg>Mamuju, Indonesia
        </div>
      </div>
      <div class="field" style="left:288px">
        <div class="field-label">Date</div>
        <div class="field-value">
          <svg viewBox="0 0 16 16"><rect x="1" y="3" width="14" height="12" rx="1.5"/><rect x="4" y="0.5" width="2" height="4" rx="1"/><rect x="10" y="0.5" width="2" height="4" rx="1"/></svg>August 16, 2022
        </div>
      </div>
      <div class="field" style="left:484px">
        <div class="field-label">Activity</div>
        <div class="field-value">
          <svg viewBox="0 0 16 16"><path d="M3 1h10v14l-5-4-5 4z"/></svg>Explore City
        </div>
      </div>
      <div class="field" style="left:661px">
        <div class="field-label">People</div>
        <div class="field-value">
          <svg viewBox="0 0 16 16"><circle cx="8" cy="4.5" r="3.5"/><path d="M1.5 15c0-4 3-6 6.5-6s6.5 2 6.5 6z"/></svg>20
        </div>
      </div>
      <div class="search-btn">Search For Trip</div>
    </form>
  </section>
</body>
</html>
```